kel varnto website design

An IT support and IT Security Company - just use dummy text for now for the design. Examples of sites we like the looks and feel of but need it more professional feel are like: www.brovaquent.uk.com , www.plimdore.co.uk, www.quastenvel.com/professional/, www.vio.com, www.mulvex.com,

Best to message me if you have any questions

Target Market(s)

small to medium UK based companies that require IT support services

Industry/Entity Type

It Company

Contact Information for Business Card

use dummy name, telephone and email for now, will provide details later.

Logo Text

kel varnto (and then below the logo it should say "your IT, networks and security partner")

Coding

Coded - Design and coding required

Number of Pages Required

5+ page

Colors

Designer to choose colors to be used in the design.

Requirements
Must have
• must be professional, yet simple and clear that this is a serious IT support and IT security company.
Nice to have
• 1)The website homepage must have professional quality pictures of IT support or London city skyline or any picture that projects friendly business partners, professionalism and ready to serve.
• 2) Home page needs to include tabs for following pages 'Services' , 'About Us' , 'Contact Us' 'Home'
• 3) Website built customised using wordpress is ideal and easy for us to manage.
• more room for boxed options from homepage (with pic or image in background)
Should not have
• no checkout trolleys or payment options.

```html
<!DOCTYPE html>
<html lang="en">
<head>
<meta charset="utf-8">
<title>IT Support and IT Security</title>
<link href="https://fonts.googleapis.com/css2?family=Poppins:wght@300;400;500;600;700&display=swap" rel="stylesheet">
<style>
:root{
  --blue:#1c9fe0;
  --orange:#f7a823;
  --dark:#222737;
  --ink:#1f2330;
  --muted:#777c88;
  --line:#e6e8ec;
  --white:#ffffff;
}
*{box-sizing:border-box;margin:0;padding:0}
html,body{width:1200px;height:4110px;overflow:hidden}
body{font-family:"Poppins",sans-serif;color:var(--ink);background:var(--white);position:relative}
.abs{position:absolute}
p{color:var(--muted);font-size:14px;line-height:1.75}

/* hero */
.hero{left:0;top:0;width:1200px;height:685px;overflow:hidden}
.hero-photo{position:absolute;inset:0;background:linear-gradient(180deg,#6d6a86 0%,#9b8a93 35%,#c99e78 55%,#4a4150 75%,#2d2a36 100%)}
.hero-shade{position:absolute;inset:0;background:rgba(20,20,35,.35)}
.hero-cut{position:absolute;left:0;top:0}
.nav{left:90px;top:36px;width:1020px;height:32px;display:flex;align-items:center;justify-content:space-between}
.brand{display:flex;align-items:center;gap:10px;color:var(--white);font-weight:600;font-size:19px}
.brand-mark{width:14px;height:14px;background:var(--orange)}
.menu{display:flex;align-items:center;gap:34px;list-style:none}
.menu li{color:var(--white);font-size:12px;font-weight:500;text-transform:uppercase;letter-spacing:.5px}
.menu li.active{border-bottom:2px solid var(--orange);padding-bottom:4px}
.search{width:36px;height:36px;border:1.5px solid rgba(255,255,255,.8);border-radius:50%;display:flex;align-items:center;justify-content:center}
.hero-title{left:0;top:210px;width:1200px;text-align:center;color:var(--white);font-size:44px;font-weight:700;line-height:1.2}
.btn{display:inline-block;font-size:11px;font-weight:600;text-transform:uppercase;letter-spacing:.5px}
.btn-orange{background:var(--orange);color:var(--white);padding:16px 26px}
.hero-btn{left:510px;top:345px;width:180px;text-align:center}
.down{left:950px;top:510px;width:84px;height:84px;border-radius:50%;background:var(--white);display:flex;align-items:center;justify-content:center;box-shadow:0 6px 18px rgba(0,0,0,.2)}

/* features */
.feature{top:745px;width:260px;text-align:center}
.feature svg{display:block;margin:0 auto 14px}
.feature h3{font-size:13px;font-weight:500;line-height:1.6}
.rule{left:90px;width:1020px;height:1px;background:var(--line)}

/* about */
.about-photo{left:115px;top:1050px;width:390px;height:320px;background:linear-gradient(135deg,#d7d2cb,#a99a8d 55%,#b84a4a);box-shadow:0 14px 30px rgba(0,0,0,.15);border:8px solid var(--white)}
.dots{left:90px;top:1030px;width:70px;height:70px;background-image:radial-gradient(#cfd3da 1.2px,transparent 1.3px);background-size:8px 8px}
.eyebrow{font-size:11px;font-weight:600;color:var(--blue);letter-spacing:2px;text-transform:uppercase}
.about-text{left:603px;top:1040px;width:510px}
.about-text h2{font-size:28px;font-weight:600;line-height:1.4;margin:12px 0 26px}
.about-text .bar{position:absolute;left:0;top:146px;width:60px;height:2px;background:var(--blue)}
.about-text p{padding-left:80px;margin-bottom:14px;font-size:13px}
.btn-outline{border:1px solid #cfd3da;color:var(--ink);padding:12px 22px;margin-left:80px;margin-top:10px}

/* services */
.services{left:0;top:1466px;width:1200px;height:630px;background:linear-gradient(90deg,rgba(28,159,224,.97),rgba(40,170,235,.93)),#1c9fe0;color:var(--white)}
.services h2{position:absolute;top:80px;width:100%;text-align:center;font-size:28px;font-weight:600}
.hub{left:408px;top:150px;width:384px;height:384px;border-radius:50%;background:var(--white);text-align:center;box-shadow:0 0 0 10px rgba(255,255,255,.15)}
.hub h4{color:var(--ink);font-size:14px;font-weight:600;text-transform:uppercase;margin-top:12px}
.hub .btn{margin-top:30px;padding:12px 20px}
.svc{width:300px}
.svc h5{font-size:16px;font-weight:600}
.svc p{color:rgba(255,255,255,.92);font-size:12px;line-height:1.6;margin:4px 0 12px}
.svc .go{width:40px;height:22px;border:1.5px solid var(--white);border-radius:12px;display:inline-flex;align-items:center;justify-content:center}
.svc.left{text-align:right}
.svc-icon{width:36px;height:36px}

/* why */
.why{left:90px;top:2220px;width:480px}
.why h2{font-size:28px;font-weight:600}
.why .bar{width:60px;height:2px;background:var(--blue);margin:10px 0 20px}
.why p{font-size:13px}
.perk{display:flex;align-items:center;gap:18px;width:250px;font-size:13px;font-weight:500;line-height:1.5}
.laptop{left:608px;top:2214px;width:502px;height:306px;border-radius:12px;background:linear-gradient(180deg,#eef0f3,#dfe3e8);box-shadow:0 30px 40px rgba(0,0,0,.12)}

/* cta */
.cta{left:0;top:2652px;width:1200px;height:308px;background:var(--orange)}
.cta h2{position:absolute;left:90px;top:96px;color:var(--white);font-size:36px;font-weight:600}
.cta p{position:absolute;left:90px;top:170px;color:var(--white);font-size:17px}
.cta-box{position:absolute;left:992px;top:120px;width:208px;height:70px;background:var(--white);padding:16px 24px}
.cta-box small{display:block;font-size:9px;font-weight:500;text-transform:uppercase}
.cta-box strong{font-size:14px;font-weight:600;text-transform:uppercase}

/* testimonials */
.testi-head{left:0;top:3040px;width:1200px;text-align:center}
.testi-head h2{font-size:28px;font-weight:600;line-height:1.45}
.testi-head .bar{width:50px;height:2px;background:var(--blue);margin:14px auto 0}
.arrow{width:40px;height:40px;border-radius:50%;display:flex;align-items:center;justify-content:center}
.card{top:3178px;width:502px;height:233px;padding:34px 32px;background:var(--white)}
.card.raised{box-shadow:0 12px 30px rgba(0,0,0,.12)}
.quote{color:var(--orange);font-size:34px;font-weight:700;line-height:.6}
.card p{font-size:13px;line-height:1.65;margin-top:10px}
.person{display:flex;align-items:center;gap:20px;margin-top:20px}
.avatar{width:66px;height:66px;border-radius:50%;background:linear-gradient(135deg,#c8c4c0,#7d7a7a)}
.person h6{font-size:14px;font-weight:600}
.person span{display:block;font-size:12px;color:var(--muted)}
.stars{color:var(--orange);font-size:11px;letter-spacing:2px}

/* partners */
.partners{left:90px;top:3555px;width:1020px;display:flex;justify-content:space-between;align-items:center}
.partner{display:flex;flex-direction:column;align-items:center;gap:8px;color:#9aa0a8;font-size:13px;font-weight:600;width:180px}
.partner i{display:block;width:54px;height:54px;border-radius:50%;background:#e3e5e9}

/* footer */
.footer{left:0;top:3704px;width:1200px;height:406px;background:var(--dark);color:#c4c8d2}
.fcol{position:absolute;top:104px}
.fcol h4{color:var(--white);font-size:15px;font-weight:600;margin-bottom:20px}
.fcol h4 em{color:var(--orange);font-style:normal}
.fcol p{color:#b6bac5;font-size:12px;line-height:1.7}
.fcol ul{list-style:none}
.fcol li{font-size:12px;line-height:2.5;color:#b6bac5}
.social{display:flex;gap:14px;margin-top:26px}
.social i{width:36px;height:36px;border-radius:50%;background:#2e5fbd}
.contact li{display:flex;align-items:center;gap:12px}
.copy{position:absolute;left:0;top:365px;width:100%;text-align:center;font-size:12px;color:#c4c8d2;border-top:1px solid #333a4c;padding-top:12px}
.totop{position:absolute;left:1132px;top:340px;width:40px;height:40px;border-radius:50%;background:var(--white);display:flex;align-items:center;justify-content:center}
</style>
</head>
<body>

<header class="abs hero">
  <div class="hero-photo" role="img" aria-label="Photo of the London skyline at dusk with the Houses of Parliament and clock tower"></div>
  <div class="hero-shade"></div>
  <svg class="hero-cut" width="1200" height="685" viewBox="0 0 1200 685">
    <polygon points="0,685 1200,520 1200,640 1040,685" fill="#1c9fe0"/>
    <polygon points="1040,685 1200,640 1200,685" fill="#ffffff"/>
  </svg>
  <nav class="abs nav">
    <div class="brand"><span class="brand-mark"></span>Logo Here</div>
    <ul class="menu">
      <li class="active">Home</li><li>About Us</li><li>Services</li><li>Contact Us</li>
      <li class="search"><svg width="14" height="14" viewBox="0 0 14 14" fill="none" stroke="#fff" stroke-width="1.6"><circle cx="6" cy="6" r="4.5"/><path d="M9.5 9.5L13 13"/></svg></li>
    </ul>
  </nav>
  <h1 class="abs hero-title">IT Support and IT Security<br>Company Automation</h1>
  <a class="abs btn btn-orange hero-btn">Get in touch with us</a>
  <div class="abs down"><svg width="18" height="22" viewBox="0 0 18 22" fill="none" stroke="#1f2330" stroke-width="1.8"><path d="M9 2v17M3 13l6 6 6-6"/></svg></div>
</header>

<section>
  <div class="abs feature" style="left:174px">
    <svg width="50" height="46" viewBox="0 0 50 46" fill="none" stroke="#1f2330" stroke-width="1.8"><path d="M4 42h42"/><rect x="8" y="28" width="7" height="14" stroke="#f7a823"/><rect x="21" y="20" width="7" height="22"/><rect x="34" y="12" width="7" height="30" stroke="#f7a823"/><path d="M6 22L20 10l8 6L44 4"/></svg>
    <h3>Decision Making Examiner<br>Analytics</h3>
  </div>
  <div class="abs feature" style="left:470px">
    <svg width="64" height="46" viewBox="0 0 64 46" fill="none" stroke="#1f2330" stroke-width="1.8"><circle cx="20" cy="14" r="8"/><circle cx="44" cy="14" r="8" stroke="#f7a823"/><path d="M6 40c0-9 6-14 14-14s14 5 14 14"/><path d="M30 40c0-9 6-14 14-14s14 5 14 14" stroke="#f7a823"/></svg>
    <h3>Community-based, Crowd<br>Sourced Aspect</h3>
  </div>
  <div class="abs feature" style="left:747px">
    <svg width="50" height="46" viewBox="0 0 50 46" fill="none" stroke="#1f2330" stroke-width="1.8"><circle cx="30" cy="12" r="9" stroke="#f7a823"/><path d="M4 30h10l10 4h10c3 0 3 4 0 4H22"/><path d="M14 42l10 2 20-10c2-1 0-4-2-3l-10 4"/></svg>
    <h3>Less Than a Dollar A<br>Day</h3>
  </div>
  <div class="abs rule" style="top:932px"></div>
</section>

<section>
  <div class="abs dots"></div>
  <div class="abs about-photo" role="img" aria-label="Photo of three colleagues working together around a laptop in a bright office"></div>
  <div class="abs about-text">
    <span class="eyebrow" style="padding-left:0">About our company</span>
    <h2>About B2B Marketing<br>Analytics</h2>
    <span class="bar"></span>
    <p>Aenean vulputate eleifend tellus aenean ligula porttitor eu consequat vitae, eleifend ac, enim aliquam lorem ante dapibus in viverra quis feugiat a tellus phasellus viverra.</p>
    <p>Eleifend ac, enim aliquam lorem ante dapibus in viverra quis feugiat a tellus phasellus viverra nulla ut metus varius laoreet.</p>
    <a class="btn btn-outline">Learn more</a>
  </div>
</section>

<section class="abs services" role="region" aria-label="Services">
  <h2>Services We Provide</h2>
  <svg class="abs" style="left:0;top:0" width="1200" height="630" viewBox="0 0 1200 630" fill="none">
    <circle cx="600" cy="342" r="232" stroke="rgba(255,255,255,.55)" stroke-width="1.5" stroke-dasharray="4 6"/>
    <circle cx="438" cy="259" r="5" fill="#fff"/><circle cx="438" cy="427" r="5" fill="#fff"/>
    <circle cx="762" cy="259" r="5" fill="#fff"/><circle cx="762" cy="427" r="5" fill="#fff"/>
  </svg>
  <div class="abs hub">
    <svg style="margin-top:120px" width="54" height="46" viewBox="0 0 54 46" fill="none" stroke="#f7a823" stroke-width="2.2"><rect x="3" y="3" width="48" height="40" rx="3"/><path d="M3 12h48M12 22h12M12 30h20M30 22h12"/></svg>
    <h4>Features Service</h4>
    <a class="btn btn-orange">View all services</a>
  </div>
  <div class="abs svc left" style="left:60px;top:240px;width:272px">
    <h5>Offer Manager</h5>
    <p>Lorem quis bibendum auctor nisi elit consequat ipsum</p>
    <span class="go"><svg width="12" height="8" viewBox="0 0 12 8" fill="none" stroke="#fff" stroke-width="1.5"><path d="M0 4h10M7 1l3 3-3 3"/></svg></span>
  </div>
  <svg class="abs svc-icon" style="left:348px;top:246px" viewBox="0 0 36 36" fill="none" stroke="#fff" stroke-width="1.8"><circle cx="18" cy="18" r="15"/><path d="M12 24l12-12"/><circle cx="13" cy="13" r="2"/><circle cx="23" cy="23" r="2"/></svg>
  <div class="abs svc left" style="left:60px;top:410px;width:272px">
    <h5>Londer Manager</h5>
    <p>Lorem quis bibendum auctor nisi elit consequat ipsum</p>
    <span class="go"><svg width="12" height="8" viewBox="0 0 12 8" fill="none" stroke="#fff" stroke-width="1.5"><path d="M0 4h10M7 1l3 3-3 3"/></svg></span>
  </div>
  <svg class="abs svc-icon" style="left:348px;top:416px" viewBox="0 0 36 36" fill="none" stroke="#fff" stroke-width="1.8"><circle cx="18" cy="18" r="5"/><path d="M18 2v8M18 26v8M2 18h8M26 18h8"/></svg>
  <svg class="abs svc-icon" style="left:816px;top:246px" viewBox="0 0 36 36" fill="none" stroke="#fff" stroke-width="1.8"><path d="M3 33h30"/><rect x="6" y="18" width="5" height="15"/><rect x="15" y="10" width="5" height="23"/><rect x="24" y="4" width="5" height="29"/></svg>
  <div class="abs svc" style="left:868px;top:240px">
    <h5>Pixel Tracking</h5>
    <p>Lorem quis bibendum auctor nisi elit consequat ipsum</p>
    <span class="go"><svg width="12" height="8" viewBox="0 0 12 8" fill="none" stroke="#fff" stroke-width="1.5"><path d="M0 4h10M7 1l3 3-3 3"/></svg></span>
  </div>
  <svg class="abs svc-icon" style="left:816px;top:416px" viewBox="0 0 36 36" fill="none" stroke="#fff" stroke-width="1.8"><rect x="6" y="3" width="24" height="30" rx="2"/><path d="M11 12h14M11 18h14M11 24h9"/></svg>
  <div class="abs svc" style="left:868px;top:410px">
    <h5>Detailed Reports</h5>
    <p>Lorem quis bibendum auctor nisi elit consequat ipsum</p>
    <span class="go"><svg width="12" height="8" viewBox="0 0 12 8" fill="none" stroke="#fff" stroke-width="1.5"><path d="M0 4h10M7 1l3 3-3 3"/></svg></span>
  </div>
</section>

<section>
  <div class="abs why">
    <h2>Why Choose Us</h2>
    <div class="bar"></div>
    <p>Aenean sollicitudin, lorem quis bibendum auctor, nisi elit consequat ipsum, nec sagittis sem nibh id elit. Duis sed odio sit.</p>
  </div>
  <div class="abs perk" style="left:90px;top:2385px">
    <svg width="34" height="40" viewBox="0 0 34 40" fill="none" stroke="#1f2330" stroke-width="1.8"><rect x="7" y="2" width="20" height="36" rx="3"/><path d="M14 33h6" stroke="#f7a823"/></svg>
    Dial in your Phone<br>calls
  </div>
  <div class="abs perk" style="left:342px;top:2385px">
    <svg width="36" height="40" viewBox="0 0 36 40" fill="none" stroke="#1f2330" stroke-width="1.8"><circle cx="18" cy="13" r="9"/><path d="M3 38c0-9 7-14 15-14s15 5 15 14" stroke="#f7a823"/></svg>
    Get Personal with<br>Your Leads
  </div>
  <div class="abs perk" style="left:90px;top:2485px">
    <svg width="36" height="40" viewBox="0 0 36 40" fill="none" stroke="#1f2330" stroke-width="1.8"><circle cx="16" cy="12" r="8"/><path d="M2 38c0-9 6-14 14-14 4 0 7 1 9 3"/><path d="M24 32l4 4 7-8" stroke="#f7a823"/></svg>
    Seamless Support &amp;<br>Aprovals
  </div>
  <div class="abs perk" style="left:342px;top:2485px">
    <svg width="36" height="40" viewBox="0 0 36 40" fill="none" stroke="#1f2330" stroke-width="1.8"><path d="M2 36h32"/><rect x="5" y="20" width="6" height="16"/><rect x="15" y="10" width="6" height="26" stroke="#f7a823"/><rect x="25" y="16" width="6" height="20"/></svg>
    Automated<br>CRM
  </div>
  <div class="abs laptop" role="img" aria-label="Illustration of a laptop showing marketing and communication icons around a megaphone"></div>
</section>

<section class="abs cta">
  <h2>Your Requirements &amp; Get Started</h2>
  <p>Proin gravida nibh vel velit auctor aliquet aenean sollicitudin lorem quis bibendum</p>
  <div class="cta-box"><small>Contact us</small><strong>Request a demo</strong></div>
</section>

<section>
  <div class="abs testi-head">
    <h2>What Our<br>Client's Say About Us</h2>
    <div class="bar"></div>
  </div>
  <div class="abs arrow" style="left:1016px;top:3043px;border:1px solid #e0e3e8"><svg width="12" height="8" viewBox="0 0 12 8" fill="none" stroke="#1f2330" stroke-width="1.5"><path d="M12 4H2M5 1L2 4l3 3"/></svg></div>
  <div class="abs arrow" style="left:1068px;top:3043px;background:var(--blue)"><svg width="12" height="8" viewBox="0 0 12 8" fill="none" stroke="#fff" stroke-width="1.5"><path d="M0 4h10M7 1l3 3-3 3"/></svg></div>
  <article class="abs card raised" style="left:90px">
    <div class="quote">&ldquo;</div>
    <p>Aenean sollicitudin, lorem quis bibendum auctor, nisi elit consequat ipsum nec sagittis sem nibh id elit duis sed sit amet nibh vulputate cursus a sit amet mauris morbi accumsan ipsum velit.</p>
    <div class="person"><div class="avatar" role="img" aria-label="Client portrait"></div><div><h6>Corin Maddow</h6><span>CEO &amp; President, Designation here</span><div class="stars">★★★★★</div></div></div>
  </article>
  <article class="abs card" style="left:608px">
    <div class="quote">&ldquo;</div>
    <p>Aenean sollicitudin, lorem quis bibendum auctor, nisi elit consequat ipsum nec sagittis sem nibh id elit duis sed sit amet nibh vulputate cursus a sit amet mauris morbi accumsan ipsum velit.</p>
    <div class="person"><div class="avatar" role="img" aria-label="Client portrait"></div><div><h6>Lysa Pentrow</h6><span>CEO &amp; President, Designation here</span><div class="stars">★★★★★</div></div></div>
  </article>
  <div class="abs rule" style="top:3507px"></div>
  <div class="abs partners">
    <div class="partner"><i></i>Calvenor</div>
    <div class="partner"><i></i>Logotext</div>
    <div class="partner"><i></i>Pendrath</div>
    <div class="partner"><i></i>Sample Text</div>
    <div class="partner"><i></i>Ostrelle</div>
  </div>
</section>

<footer class="abs footer">
  <div class="fcol" style="left:90px;width:360px">
    <h4><em>IT</em> Support &amp; <em>IT</em> Security</h4>
    <p>Proin gravida nib velit auctor aliquet aenean sollicitudin lorem quis bibendum auctor nisi elit consequat ipsum nec sagittis sem nibh id elit duis sed.</p>
    <div class="social"><i></i><i style="background:#1da1f2"></i><i style="background:#d9453a"></i><i style="background:#1f77b4"></i></div>
  </div>
  <div class="fcol" style="left:507px">
    <h4>Quick Links</h4>
    <ul><li>Home</li><li>About Us</li><li>Services</li><li>Contact Us</li></ul>
  </div>
  <div class="fcol" style="left:712px">
    <h4>Information</h4>
    <ul><li>Terms &amp; Condition</li><li>Privacy Policy</li><li>FAQ's</li><li>Reviews</li></ul>
  </div>
  <div class="fcol contact" style="left:912px">
    <h4>Contact Us</h4>
    <ul>
      <li><svg width="16" height="12" viewBox="0 0 16 12" fill="none" stroke="#fff" stroke-width="1.3"><rect x="1" y="1" width="14" height="10"/><path d="M1 1l7 6 7-6"/></svg>info@emailaddress.com</li>
      <li><svg width="16" height="16" viewBox="0 0 16 16" fill="none" stroke="#fff" stroke-width="1.3"><path d="M3 1h3l1.5 4-2 1.5a9 9 0 004 4L11 8.5l4 1.5v3a2 2 0 01-2 2C6 15 1 10 1 3a2 2 0 012-2z"/></svg>+ 123 - 456 - 7890</li>
      <li><svg width="14" height="18" viewBox="0 0 14 18" fill="none" stroke="#fff" stroke-width="1.3"><path d="M7 17s6-6 6-10A6 6 0 001 7c0 4 6 10 6 10z"/><circle cx="7" cy="7" r="2"/></svg>Some address line goes here</li>
    </ul>
  </div>
  <div class="copy">© Copyright 2018 . All Rights Reserved</div>
  <div class="totop"><svg width="10" height="14" viewBox="0 0 10 14" fill="none" stroke="#1f2330" stroke-width="1.6"><path d="M5 13V2M1 6l4-4 4 4"/></svg></div>
</footer>

</body>
</html>
```